Marlowvex Website Concept

We would like a one page website. Please refer to the attached files for more information.

Please reference file attachment version 1.1.

```html
<!DOCTYPE html>
<html lang="en">
<head>
<meta charset="utf-8">
<title>Marlowvex — Company Description</title>
<link rel="stylesheet" href="https://fonts.googleapis.com/css2?family=Montserrat:wght@700;800&family=Oswald:wght@500;600&family=Open+Sans:wght@400;600&family=Arimo:wght@400&display=swap">
<style>
  :root {
    --hero-black: #050505;
    --hero-glow: #1b1f24;
    --title-white: #ffffff;
    --accent-blue: #1e9fd6;
    --nav-bg: #f4f5f6;
    --nav-text: #2e2e2e;
    --nav-sep: #9a9a9a;
    --content-navy: #06101f;
    --content-blue: #0f2a4c;
    --body-text: #f2f4f7;
    --social-dot: #3a4a5c;
  }
  * { margin: 0; padding: 0; box-sizing: border-box; }
  html, body { width: 1159px; height: 1200px; overflow: hidden; background: var(--hero-black); }
  .page { position: relative; width: 1159px; height: 1200px; }

  .hero {
    position: absolute; left: 0; top: 0; width: 1159px; height: 622px;
    background: var(--hero-black);
  }
  .hero-visual {
    position: absolute; left: 0; top: 0; width: 1159px; height: 622px;
    background:
      radial-gradient(ellipse 22% 40% at 62% 28%, rgba(120,200,235,0.16), transparent 70%),
      radial-gradient(ellipse 20% 30% at 72% 62%, rgba(200,160,130,0.22), transparent 70%),
      radial-gradient(ellipse 30% 28% at 92% 92%, rgba(40,55,80,0.55), transparent 75%),
      var(--hero-black);
  }
  .hero-rule {
    position: absolute; left: 446px; top: 187px; width: 2px; height: 252px;
    background: var(--accent-blue);
  }
  .hero-title {
    position: absolute; left: 79px; top: 288px;
    font-family: "Montserrat", sans-serif; font-weight: 800;
    font-size: 44px; line-height: 44px; letter-spacing: 3px; color: var(--title-white);
    white-space: nowrap;
  }

  .site-nav {
    position: absolute; left: 0; top: 622px; width: 1159px; height: 84px;
    background: var(--nav-bg); border-bottom: 3px solid var(--accent-blue);
  }
  .brand {
    position: absolute; left: 28px; top: 14px; height: 54px;
    display: flex; align-items: center; gap: 10px;
  }
  .brand-mark { width: 38px; height: 38px; border-radius: 50%; background: var(--content-blue); }
  .brand-name {
    font-family: "Open Sans", sans-serif; font-weight: 600; font-size: 28px;
    color: var(--content-blue); letter-spacing: 0.5px;
  }
  .nav-menu {
    position: absolute; left: 340px; top: 0; height: 84px;
    display: flex; align-items: center; list-style: none;
    font-family: "Open Sans", sans-serif; font-size: 13px; color: var(--nav-text);
  }
  .nav-menu li { padding: 0 22px; border-right: 1px solid var(--nav-sep); line-height: 16px; }
  .nav-menu li:first-child { padding-left: 14px; }
  .social-links {
    position: absolute; left: 940px; top: 32px; display: flex; gap: 9px; align-items: center;
  }
  .social-dot { width: 20px; height: 20px; border-radius: 50%; background: var(--social-dot); }
  .nav-divider { position: absolute; left: 1066px; top: 30px; width: 1px; height: 24px; background: var(--accent-blue); }
  .search-icon { position: absolute; left: 1090px; top: 35px; }

  .company {
    position: absolute; left: 0; top: 709px; width: 1159px; height: 491px;
    background:
      radial-gradient(ellipse 30% 50% at 50% 45%, rgba(90,120,160,0.35), transparent 70%),
      radial-gradient(ellipse 25% 40% at 20% 95%, rgba(180,140,60,0.25), transparent 70%),
      linear-gradient(180deg, var(--content-navy), var(--content-blue) 60%, var(--content-navy));
  }
  .section-title {
    position: absolute; left: 0; top: 48px; width: 1159px; text-align: center;
    font-family: "Oswald", sans-serif; font-weight: 600; font-size: 30px;
    color: var(--title-white);
  }
  .section-rule {
    position: absolute; left: 390px; top: 97px; width: 388px; height: 2px;
    background: var(--accent-blue);
  }
  .section-copy {
    position: absolute; left: 100px; top: 148px; width: 955px;
    font-family: "Arimo", Arial, sans-serif; font-size: 13.6px; line-height: 20.5px;
    color: var(--body-text); text-align: justify;
  }
  .section-copy p { margin-bottom: 20.5px; }
</style>
</head>
<body>
<div class="page">
  <header class="hero">
    <div class="hero-visual" role="img" aria-label="Photo of a hand in a suit sleeve gripping glowing arrows labelled protection, security, dossier creation and threat assessment"></div>
    <div class="hero-rule"></div>
    <h1 class="hero-title">MARLOWVEX</h1>
  </header>

  <nav class="site-nav">
    <div class="brand">
      <span class="brand-mark"></span>
      <span class="brand-name">Marlowvex</span>
    </div>
    <ul class="nav-menu">
      <li>COMPANY DESCRIPTION</li>
      <li>SERVICE OFFERINGS</li>
      <li>WEBSITE LEAD CAPTURE</li>
    </ul>
    <div class="social-links">
      <span class="social-dot"></span><span class="social-dot"></span>
      <span class="social-dot"></span><span class="social-dot"></span>
    </div>
    <div class="nav-divider"></div>
    <svg class="search-icon" width="14" height="14" viewBox="0 0 14 14" aria-label="Search">
      <circle cx="5.5" cy="5.5" r="4" fill="none" stroke="#222" stroke-width="2"/>
      <line x1="8.5" y1="8.5" x2="13" y2="13" stroke="#222" stroke-width="2.2" stroke-linecap="round"/>
    </svg>
  </nav>

  <section class="company" role="img" aria-label="Dim city skyline photo behind the company description">
    <h2 class="section-title">COMPANY DESCRIPTION</h2>
    <div class="section-rule"></div>
    <div class="section-copy">
      <p>Marlowvex is a United States-based tier one security firm specializing in the protection of financial services professionals, executives and their families. We manage engagements resulting from general and specific threats throughout the United States and abroad on behalf of our domestic clients. We deliver our services exclusively through associates and contractors with United States special operations, secret service, CIA, or equivalent experience and training. We are one of only a handful of domestic security firms that offers scalable, tier one security services in every market in the United States.</p>
      <p>If you have a general or specific threat you would like to have assessed, it will be our privilege to evaluate your circumstances and provide you with an opinion of how to best address your security needs. Not all security circumstances require tier one professionals. It will be our pleasure to direct you to other firms in your market if you or we believe our service levels are not warranted.</p>
      <p>Our firm was created as the result of a specific threat to two of our founders resulting from a private equity transaction with a hostile seller. If you are a transaction professional or executive who is experiencing the fear and uncertainty of the risks associated with a general or specific security threat, it will be our privilege to help you manage this challenging process.</p>
    </div>
  </section>
</div>
</body>
</html>
```